Cage Free Dog Resort under new ownership needs New Logo & Website Redesign

We need a logo design and updated website for our new business. We offer cage free boarding services for dogs where they are free to run & play outside during the day. The current website has lots of brown & orange & we would like the new website to be more visually attractive utilizing more pictures of dogs playing and having fun.

Target Market(s)

Dog lovers with disposable income to afford special care for their pets - looking for a place for their dogs to be pampered while they are away from home. Primarily dogs, but we will also board cats and other pets too.

Industry/Entity Type

Pet Care

Logo Text

Willow Creek Pet Lodge

Coding

Coded - Design and coding required

Number of Pages Required

5+ page

Font styles to use
Sans Serif

Colors
0692cd
fbee3d
f04a50

Requirements
Must have
• Current website is www.willowcreekpetlodge.example
• I would like for someone to click on our website & have the "oh that is so cute/awesome/what a great looking place" reaction!
• Link to pages with forms
• Stock photos of different breeds of dogs having fun playing out doors
• Gallery Photo page (where I can go in and update with new pictures)
Nice to have
• Tag line something like - "Your best friend's home away from home!"
• Some cartoon type dogs/cats
Should not have
• Wasn't sure about font below - so whichever font is easiest to read and still looks professional

```html
<!DOCTYPE html>
<html lang="en">
<head>
<meta charset="utf-8">
<title>Willow Creek Pet Lodge &amp; doggie daycare</title>
<link rel="stylesheet" href="https://fonts.googleapis.com/css2?family=Roboto:wght@300;400;500;700&family=Open+Sans:wght@400;600&display=swap">
<style>
:root{
  --red:#d3213b;
  --red-bright:#f04a50;
  --blue:#0b6fb8;
  --blue-light:#0692cd;
  --sand:#f6e2a8;
  --ink:#1e1e1e;
  --text:#555;
  --white:#fff;
  --black:#0d0d0d;
  --grey:#bbb;
}
*{margin:0;padding:0;box-sizing:border-box}
html,body{width:1200px;height:4651px;overflow:hidden}
body{position:relative;font-family:"Open Sans",sans-serif;color:var(--ink);background:var(--white)}
.abs{position:absolute}
h1,h2,h3,h4,.nav,.brand{font-family:"Roboto",sans-serif}

/* header */
.top-line{left:0;top:0;width:1200px;height:7px;background:var(--red)}
.site-header{left:0;top:7px;width:1200px;height:133px;background:var(--white)}
.brand{left:88px;top:38px;display:flex;align-items:center;gap:18px}
.brand-dot{width:56px;height:56px;border-radius:50%;background:var(--red)}
.brand-name{font-size:21px;font-weight:500;line-height:28px;color:var(--ink)}
.nav{right:92px;top:56px;display:flex;gap:52px;font-size:17px;font-weight:500}
.nav a{color:var(--ink);text-decoration:none}
.nav a.active{color:var(--red)}

/* hero */
.hero{left:0;top:140px;width:1200px;height:590px;background:linear-gradient(180deg,#aab9c4 0%,#8ea18a 45%,#5f8a3c 75%,#4e7a2f 100%)}
.hero-title{left:93px;top:330px;color:var(--white);font-family:"Roboto",sans-serif;font-weight:700;text-shadow:0 2px 6px rgba(0,0,0,.45)}
.hero-title .l1{display:block;font-size:52px;line-height:60px}
.hero-title .l2{display:block;font-size:42px;line-height:52px}
.dots{left:1150px;top:388px;display:flex;flex-direction:column;gap:14px}
.dots span{width:8px;height:8px;border-radius:50%;background:rgba(255,255,255,.6)}
.dots span:first-child{background:var(--white)}

/* intro */
.intro-art{left:31px;top:800px;width:140px;height:145px;border-radius:12px;background:linear-gradient(135deg,#c7874b,#f2ede4)}
.intro-title{left:0;width:1200px;top:838px;text-align:center;font-size:33px;font-weight:500}
.intro-text{left:170px;width:860px;top:898px;text-align:center;font-size:15px;line-height:24px;color:var(--text)}

.feature{top:1075px;width:300px;text-align:center}
.feature-icon{width:96px;height:96px;margin:0 auto;border-radius:50%;background:var(--white);box-shadow:0 3px 12px rgba(0,0,0,.15);display:flex;align-items:center;justify-content:center}
.feature h3{margin-top:52px;font-size:21px;font-weight:500}
.feature p{margin-top:12px;font-size:14.5px;line-height:22px;color:var(--text)}
.feature .chev{margin-top:18px}
.intro-pup{left:1025px;top:1339px;width:122px;height:124px;border-radius:14px;background:linear-gradient(135deg,#b9733c,#f3ede2)}

/* about */
.about{left:0;top:1482px;width:1200px;height:601px;background:radial-gradient(circle at 25% 45%,#e5d3b8 0 14%,#6e9a3a 34%,#3f6e22 100%)}
.about-title{left:580px;top:1612px;color:var(--white);font-size:37px;font-weight:500}
.about-text{left:580px;top:1670px;width:490px;color:var(--white);font-size:14.5px;line-height:25px}
.btn{display:inline-block;background:var(--red);color:var(--white);border-radius:16px;font-family:"Roboto",sans-serif;font-size:13px;font-weight:500;padding:7px 22px;text-decoration:none}
.about-btn{left:580px;top:1868px}

/* blog */
.blog-title{left:0;width:1200px;top:2228px;text-align:center;font-size:37px;font-weight:500}
.blog-sub{left:0;width:1200px;top:2282px;text-align:center;font-size:21px;font-family:"Roboto",sans-serif}
.card{top:2362px;width:322px;height:413px;background:var(--white);box-shadow:0 4px 14px rgba(0,0,0,.18);text-align:center}
.card-photo{width:100%;height:217px}
.card h4{margin-top:30px;font-size:19px;font-weight:500}
.card p{margin:14px 30px 0;font-size:13.5px;line-height:22px;color:var(--text)}
.card .btn{margin-top:20px}
.blog-cat{left:992px;top:2805px;width:171px;height:135px;border-radius:14px;background:linear-gradient(135deg,#8a7a9e,#c6bcd4)}

/* testimonials */
.testimonials{left:0;top:2939px;width:1200px;height:580px;background:linear-gradient(180deg,#0f5da6,#0b6fb8 60%,#1565a8)}
.testi-title{left:0;width:1200px;top:3040px;text-align:center;color:var(--white);font-size:36px;font-weight:400}
.testi{top:3156px;width:450px;height:214px;background:var(--white);border-radius:10px;box-shadow:0 4px 14px rgba(0,0,0,.25)}
.testi-photo{position:absolute;left:-18px;top:50px;width:120px;height:120px;border-radius:50%;border:6px solid var(--white);background:linear-gradient(135deg,#9d7a58,#e0c9a8)}
.testi h4{position:absolute;left:112px;top:42px;font-size:18px;font-weight:500}
.testi p{position:absolute;left:112px;top:80px;width:290px;font-size:14px;line-height:22px;color:var(--text)}
.testi .who{position:absolute;right:50px;top:176px;font-size:16px;color:var(--blue-light)}
.quote{position:absolute;right:36px;top:32px}

/* gallery */
.gallery-bg{left:0;top:3500px;width:1200px;height:780px;background:var(--sand)}
.gallery-title{left:66px;top:3712px;font-size:37px;font-weight:500}
.thumb{top:3788px;width:233px;height:264px}
.view-more{left:660px;top:4074px;font-size:14px;color:var(--red);text-decoration:none;font-family:"Roboto",sans-serif}
.gallery-art{left:760px;top:3751px;width:434px;height:403px;border-radius:50% 50% 8px 8px;background:radial-gradient(circle at 55% 40%,#f8e7a0 0 35%,#d67f2f 60%,#9b4d1e 100%)}

/* footer */
.site-footer{left:0;top:4290px;width:1200px;height:361px;background:var(--black);color:var(--grey)}
.fcol{top:90px}
.fcol h4{font-size:15px;font-weight:500;color:var(--white);margin-bottom:22px;letter-spacing:.3px}
.fcol ul{list-style:none;font-size:13px;line-height:24px}
.fcol li::before{content:"» ";color:var(--white)}
.contact li::before{content:none}
.contact li{display:flex;align-items:center;gap:14px;margin-bottom:10px}
.mail-form{margin-top:18px;width:220px;height:42px;border:1px solid #888;border-radius:22px;display:flex;align-items:center;justify-content:space-between;padding:0 12px 0 18px;font-size:13px}
.mail-go{width:18px;height:18px;border-radius:50%;background:var(--grey)}
.foot-rule{left:112px;top:268px;width:976px;height:1px;background:#2c2c2c}
.copyright{left:0;width:1200px;top:292px;text-align:center;font-size:13px;color:var(--grey)}
</style>
</head>
<body>

<div class="abs top-line"></div>
<header class="abs site-header">
  <div class="abs brand" style="top:31px">
    <span class="brand-dot"></span>
    <span class="brand-name">Willow Creek Pet Lodge<br>&amp; doggie daycare</span>
  </div>
  <nav class="abs nav" style="top:49px">
    <a class="active" href="#">Home</a><a href="#">Profiles</a><a href="#">Stories</a><a href="#">Community</a><a href="#">Blog</a><a href="#">Contact</a>
  </nav>
</header>

<section class="abs hero" role="img" aria-label="Photo of a happy white and brown dog bounding across a green park lawn with its owner behind"></section>
<h1 class="abs hero-title"><span class="l1">Your best friend's</span><span class="l2">home away from home!</span></h1>
<div class="abs dots"><span></span><span></span><span></span><span></span></div>
<svg class="abs" style="left:0;top:620px" width="1200" height="112" viewBox="0 0 1200 112">
  <polygon points="0,28 680,112 0,112" fill="var(--red)"/>
  <polygon points="0,70 0,112 1200,112 1200,78 640,112" fill="var(--white)"/>
</svg>

<div class="abs intro-art" role="img" aria-label="Cartoon beagle puppy sitting"></div>
<h2 class="abs intro-title">Willow Creek Pet Lodge &amp; doggie daycare</h2>
<p class="abs intro-text">Willow Creek Pet Lodge started when, being the animal lover I am, I started pet-sitting in my home for teachers when they went on vacation. I quickly saw the need for real home-based pet care and knew how I wanted to do it. This involved selling my home in Maple Falls, cashing out my retirement and buying a little ranch-style home on two acres in Cedar Grove.</p>

<div class="abs feature" style="left:98px">
  <div class="feature-icon"><svg width="50" height="50" viewBox="0 0 50 50"><path d="M25 45 L6 26 A11 11 0 0 1 25 12 A11 11 0 0 1 44 26 Z" fill="var(--blue)"/><circle cx="25" cy="30" r="5" fill="#fff"/><circle cx="18" cy="23" r="2.6" fill="#fff"/><circle cx="22.5" cy="19" r="2.6" fill="#fff"/><circle cx="27.5" cy="19" r="2.6" fill="#fff"/><circle cx="32" cy="23" r="2.6" fill="#fff"/></svg></div>
  <h3>Services</h3>
  <p>Lorem Ipsum has been the industry's<br>standard dummy text ever since the<br>1500s, when an unknown</p>
  <svg class="chev" width="20" height="20" viewBox="0 0 20 20"><path d="M4 3l6 6 6-6M4 10l6 6 6-6" fill="none" stroke="var(--blue-light)" stroke-width="2.4"/></svg>
</div>
<div class="abs feature" style="left:448px">
  <div class="feature-icon"><svg width="50" height="50" viewBox="0 0 50 50"><circle cx="20" cy="10" r="5" fill="var(--blue)"/><path d="M14 17h12v14l6 10h-6l-5-9-3 9h-6l4-12z" fill="var(--blue)"/><path d="M30 30h12v5h-3v8h-3v-8h-3v8h-3z" fill="var(--blue)"/><circle cx="42" cy="27" r="3" fill="var(--blue)"/></svg></div>
  <h3>Rates and Hours</h3>
  <p>Lorem Ipsum has been the industry's<br>standard dummy text ever since the<br>1500s, when an unknown</p>
  <svg class="chev" width="20" height="20" viewBox="0 0 20 20"><path d="M4 3l6 6 6-6M4 10l6 6 6-6" fill="none" stroke="var(--blue-light)" stroke-width="2.4"/></svg>
</div>
<div class="abs feature" style="left:796px">
  <div class="feature-icon"><svg width="50" height="50" viewBox="0 0 50 50"><path d="M25 6L4 24h6v20h30V24h6z" fill="var(--blue)"/><rect x="20" y="30" width="10" height="14" fill="#fff"/><rect x="13" y="27" width="5" height="5" fill="#fff"/><rect x="32" y="27" width="5" height="5" fill="#fff"/></svg></div>
  <h3>Accommodations</h3>
  <p>Lorem Ipsum has been the industry's<br>standard dummy text ever since the<br>1500s, when an unknown</p>
  <svg class="chev" width="20" height="20" viewBox="0 0 20 20"><path d="M4 3l6 6 6-6M4 10l6 6 6-6" fill="none" stroke="var(--blue-light)" stroke-width="2.4"/></svg>
</div>
<div class="abs intro-pup" role="img" aria-label="Cartoon puppy peeking in"></div>

<section class="abs about" role="img" aria-label="Photo of a smiling beagle mix lying on green grass"></section>
<h2 class="abs about-title">About us</h2>
<p class="abs about-text">It is a long established fact that a reader will be distracted by the readable content of a page when looking at its layout. The point of using Lorem Ipsum is that it has a more-or-less normal distribution of letters, as opposed to using 'Content here, content here', making it look like readable English. Many desktop publishing packages and web page editors now use Lorem Ipsum as their default model text, and a search for 'lorem ipsum' will uncover many web sites still in their infancy.</p>
<a class="abs btn about-btn" href="#">View More</a>
<svg class="abs" style="left:0;top:1983px" width="1200" height="102" viewBox="0 0 1200 102">
  <polygon points="680,102 1200,0 1200,102" fill="var(--blue)"/>
  <polygon points="0,85 1200,40 1200,102 0,102" fill="var(--white)" opacity="0"/>
</svg>

<h2 class="abs blog-title">Latest Blog</h2>
<p class="abs blog-sub">Neque porro quisquam est qui dolorem</p>

<article class="abs card" style="left:93px">
  <div class="card-photo" role="img" aria-label="Photo of dogs playing together in a snowy yard" style="background:linear-gradient(135deg,#d9d4cf,#6b625a)"></div>
  <h4>Neque porro quisquam</h4>
  <p>It is a long established fact that a reader will be distracted by the readable content of a page when looking at its layout</p>
  <a class="btn" href="#">View More</a>
</article>
<article class="abs card" style="left:434px">
  <div class="card-photo" role="img" aria-label="Photo of a woman cuddling a white fluffy dog" style="background:linear-gradient(135deg,#c79a7a,#f0e6da)"></div>
  <h4>Dolorem ipsum quia</h4>
  <p>It is a long established fact that a reader will be distracted by the readable content of a page when looking at its layout</p>
  <a class="btn" href="#">View More</a>
</article>
<article class="abs card" style="left:784px">
  <div class="card-photo" role="img" aria-label="Photo of a small dog beside a blue kiddie pool on a patio" style="background:linear-gradient(135deg,#8a6a4e,#7fb4d8)"></div>
  <h4>Neque porro quisquam</h4>
  <p>It is a long established fact that a reader will be distracted by the readable content of a page when looking at its layout</p>
  <a class="btn" href="#">View More</a>
</article>
<div class="abs blog-cat" role="img" aria-label="Cartoon grey cat walking"></div>

<section class="abs testimonials" role="img" aria-label="Faint photo of dogs in blue tone"></section>
<h2 class="abs testi-title">Testimonial</h2>
<div class="abs testi" style="left:130px">
  <div class="testi-photo" role="img" aria-label="Round photo of a client with a dog"></div>
  <h4>Neque porro quisquam</h4>
  <svg class="quote" width="46" height="36" viewBox="0 0 46 36"><path d="M2 34V20C2 9 8 3 18 1v7c-5 2-7 5-7 10h7v16zM26 34V20c0-11 6-17 16-19v7c-5 2-7 5-7 10h7v16z" fill="var(--red)"/></svg>
  <p>The point of using Lorem Ipsum is that it has a more-or-less normal distribution of letters, as opposed to using 'Content</p>
  <span class="who">- &nbsp;Helen</span>
</div>
<div class="abs testi" style="left:651px">
  <div class="testi-photo" role="img" aria-label="Round photo of a client with a dog"></div>
  <h4>Dolorem ipsum quia dolor</h4>
  <svg class="quote" width="46" height="36" viewBox="0 0 46 36"><path d="M2 34V20C2 9 8 3 18 1v7c-5 2-7 5-7 10h7v16zM26 34V20c0-11 6-17 16-19v7c-5 2-7 5-7 10h7v16z" fill="var(--red)"/></svg>
  <p>The point of using Lorem Ipsum is that it has a more-or-less normal distribution of letters, as opposed to using 'Content</p>
  <span class="who">- &nbsp;Amet</span>
</div>

<div class="abs gallery-bg"></div>
<svg class="abs" style="left:0;top:3430px" width="1200" height="130" viewBox="0 0 1200 130">
  <polygon points="0,0 1200,0 1200,90 0,20" fill="#1565a8"/>
  <polygon points="0,20 1200,90 1200,110 0,110" fill="var(--red)"/>
  <polygon points="0,110 1200,110 1200,130 0,130" fill="var(--sand)"/>
  <polygon points="0,110 1200,110 0,78" fill="var(--red)"/>
</svg>
<h2 class="abs gallery-title">Gallery</h2>
<div class="abs thumb" style="left:62px;background:linear-gradient(160deg,#e7a24f,#8a5a2a)" role="img" aria-label="Photo of a fluffy puppy among autumn leaves"></div>
<div class="abs thumb" style="left:301px;background:linear-gradient(160deg,#8aa64e,#9b4f22)" role="img" aria-label="Photo of two red-coated dogs in a meadow"></div>
<div class="abs thumb" style="left:543px;background:linear-gradient(160deg,#b5b2ad,#4a4642)" role="img" aria-label="Photo of a grey cat and a dog resting together"></div>
<a class="abs view-more" href="#">View More »</a>
<div class="abs gallery-art" role="img" aria-label="Cartoon brown dog hugging an orange cat in front of a yellow sun"></div>

<svg class="abs" style="left:0;top:4190px" width="1200" height="110" viewBox="0 0 1200 110">
  <polygon points="0,0 1200,60 1200,110 0,110" fill="var(--blue)"/>
  <polygon points="0,80 1200,110 0,110" fill="var(--black)"/>
</svg>

<footer class="abs site-footer">
  <div class="abs fcol" style="left:112px">
    <h4>LINKS</h4>
    <ul><li>Home</li><li>About</li><li>Blog</li><li>Contact</li></ul>
  </div>
  <div class="abs fcol" style="left:295px">
    <h4>INFORMATION</h4>
    <ul><li>Privacy Policy</li><li>Your Account</li><li>Advanced Search</li><li>Contact Us</li></ul>
  </div>
  <div class="abs fcol contact" style="left:536px">
    <h4>CONTACT US</h4>
    <ul>
      <li><svg width="12" height="16" viewBox="0 0 12 16"><path d="M6 0a6 6 0 0 0-6 6c0 4 6 10 6 10s6-6 6-10a6 6 0 0 0-6-6zm0 8.5A2.5 2.5 0 1 1 6 3.5a2.5 2.5 0 0 1 0 5z" fill="#fff"/></svg>4821 Meadow Lane, Cedar Grove TX 77000</li>
      <li><svg width="14" height="14" viewBox="0 0 14 14"><path d="M3 0l3 3-2 2c1 2 3 4 5 5l2-2 3 3-2 3C6 14 0 8 0 2z" fill="#fff"/></svg>555-014-2278</li>
      <li><svg width="16" height="12" viewBox="0 0 16 12"><rect width="16" height="12" fill="#fff"/><path d="M0 0l8 6 8-6" fill="none" stroke="#0d0d0d" stroke-width="1.4"/></svg>hello@willowcreekpetlodge.example</li>
    </ul>
  </div>
  <div class="abs fcol" style="left:871px">
    <h4>JOIN OUR MAILING LIST</h4>
    <p style="font-size:13px;line-height:22px;width:220px">Your email us information would fit here nicely.</p>
    <div class="mail-form"><span>Email address</span><span class="mail-go"></span></div>
  </div>
  <div class="abs foot-rule"></div>
  <p class="abs copyright">Copyright © 2018. All Rights Reserved</p>
</footer>

</body>
</html>
```